Education Certificate

We need a modern yet professional Certificate for those who successfully pass / complete our online Training course.

There are various courses but ONE certificate design required.

the certificate needs to look extremely professional and of value.

```html
<!DOCTYPE html>
<html lang="en">
<head>
<meta charset="UTF-8">
<title>Certificate of Training</title>
<link rel="stylesheet" href="https://fonts.googleapis.com/css2?family=Montserrat:wght@500;600;800;900&family=Pinyon+Script&family=Arimo:wght@400&display=swap">
<style>
  :root {
    --royal-blue: #1b46a3;
    --deep-blue: #1d3c8f;
    --gold: #f2c618;
    --gold-dark: #c9a227;
    --paper: #fdfdfd;
    --ink: #1a1a1a;
    --panel-border: #d9dbe0;
    --page-bg: #eeeeee;
  }
  * { margin: 0; padding: 0; box-sizing: border-box; }
  html, body {
    width: 1200px;
    height: 800px;
    overflow: hidden;
    background: var(--page-bg);
  }
  .certificate {
    position: relative;
    width: 1200px;
    height: 800px;
    background: var(--royal-blue);
    overflow: hidden;
  }
  .frame-line {
    position: absolute;
    left: 22px; top: 22px; right: 22px; bottom: 66px;
    border: 3px solid var(--gold);
    border-radius: 78px;
  }
  .paper {
    position: absolute;
    left: 36px; top: 36px; right: 36px; bottom: 80px;
    background:
      repeating-linear-gradient(90deg, rgba(40,60,110,0.05) 0 1px, transparent 1px 9px),
      var(--paper);
    border-radius: 66px;
  }
  .side-tab {
    position: absolute;
    width: 20px;
    background: var(--gold);
  }
  .side-tab--left { left: 0; top: 440px; height: 150px; }
  .side-tab--right { right: 0; top: 150px; height: 72px; }

  .title {
    position: absolute;
    top: 92px; left: 0; right: 0;
    text-align: center;
    font-family: "Montserrat", sans-serif;
    font-weight: 900;
    font-size: 104px;
    letter-spacing: 4px;
    color: var(--royal-blue);
    line-height: 1;
  }
  .subtitle {
    position: absolute;
    top: 196px; left: 0; right: 0;
    text-align: center;
    font-family: "Pinyon Script", cursive;
    font-size: 96px;
    color: var(--ink);
    line-height: 1;
  }
  .recipient {
    position: absolute;
    top: 340px; left: 340px; width: 560px;
    text-align: center;
    font-family: "Arimo", sans-serif;
    font-size: 52px;
    color: var(--deep-blue);
    padding-bottom: 14px;
    border-bottom: 2px dashed var(--gold-dark);
  }
  .completion-note {
    position: absolute;
    top: 452px; left: 0; right: 0;
    text-align: center;
    font-family: "Pinyon Script", cursive;
    font-size: 42px;
    color: var(--ink);
  }
  .course-name {
    position: absolute;
    top: 512px; left: 0; right: 0;
    text-align: center;
    font-family: "Montserrat", sans-serif;
    font-weight: 600;
    font-size: 42px;
    letter-spacing: 1px;
    color: var(--deep-blue);
  }
  .issuer {
    position: absolute;
    top: 590px; left: 470px;
    width: 280px; height: 118px;
    border: 1.5px solid var(--panel-border);
    border-radius: 14px 14px 0 0;
    border-bottom: none;
    display: flex;
    align-items: center;
    justify-content: center;
    gap: 14px;
  }
  .issuer-mark {
    width: 42px; height: 42px;
    background: var(--royal-blue);
    flex: none;
  }
  .issuer-name {
    font-family: "Montserrat", sans-serif;
    font-weight: 500;
    font-size: 15px;
    line-height: 1.25;
    text-transform: uppercase;
    color: var(--royal-blue);
  }
  .seal {
    position: absolute;
    left: 118px; top: 420px;
    width: 170px; height: 170px;
  }
  .field {
    position: absolute;
    text-align: center;
    font-family: "Arimo", sans-serif;
    color: var(--ink);
  }
  .field-value {
    font-size: 22px;
    padding: 0 8px 4px;
    border-bottom: 1.5px solid var(--ink);
  }
  .field-label {
    font-size: 19px;
    padding-top: 4px;
  }
  .field--date { left: 150px; top: 640px; width: 170px; }
  .field--signature { left: 900px; top: 580px; width: 170px; }
  .field--signature .field-value {
    font-family: "Pinyon Script", cursive;
    font-size: 44px;
    line-height: 1;
  }
  .website {
    position: absolute;
    left: 0; right: 0; bottom: 18px;
    text-align: center;
    font-family: "Montserrat", sans-serif;
    font-weight: 500;
    font-size: 30px;
    letter-spacing: 1px;
    color: var(--gold);
  }
</style>
</head>
<body>
  <main class="certificate">
    <div class="side-tab side-tab--left"></div>
    <div class="side-tab side-tab--right"></div>
    <div class="frame-line"></div>
    <div class="paper"></div>

    <h1 class="title">CERTIFICATE</h1>
    <p class="subtitle">of Training</p>

    <p class="recipient">Type your name here</p>
    <p class="completion-note">For successful completion of</p>
    <p class="course-name">COURES NAME</p>

    <svg class="seal" viewBox="0 0 170 170" role="img" aria-label="Gold award seal">
      <defs>
        <radialGradient id="sealGold" cx="40%" cy="35%" r="70%">
          <stop offset="0" stop-color="#fbe7a1"/>
          <stop offset="1" stop-color="#d0a03a"/>
        </radialGradient>
      </defs>
      <circle cx="85" cy="85" r="80" fill="url(#sealGold)"/>
      <circle cx="85" cy="85" r="62" fill="none" stroke="#1b46a3" stroke-width="6"/>
    </svg>

    <div class="issuer">
      <span class="issuer-mark"></span>
      <span class="issuer-name">Global Service<br>Excellence<br>Academy</span>
    </div>

    <div class="field field--date">
      <div class="field-value">00.00.2024</div>
      <div class="field-label">DATE</div>
    </div>

    <div class="field field--signature">
      <div class="field-value">sign</div>
      <div class="field-label">SIGNATURE</div>
    </div>

    <p class="website">www.gsea-learn.com</p>
  </main>
</body>
</html>
```